Crestline Lending Group Business Cards

We are looking to revamp the current business cards each of our locations uses. We are a lending company that specializes in personal loans, title loans, and tax services. We have locations in New Mexico, Texas, and Oklahoma.

We would like a cleaner, sleeker look while still highlighting what we offer. Title Loans, Personal Loans & Tax Services. We also want to include our referral fee somewhere on the card. We would like to see an English option as well as a Spanish option for the cards.

PLEASE NOTE: Some business cards do not include the employee's name but just the store's location, while others will include both.

These are double-sided business cards, and we would like to see proof if possible. I have included proofs of our current business cards for you to review below, as well as our company logo. Feel free to get creative with the logo, etc! Colors should match the logo; however, you do not need to use all of our logo colors if you don't want to.

```html
<!DOCTYPE html>
<html lang="en">
<head>
<meta charset="utf-8">
<title>Crestline Lending Group – Business Card</title>
<link rel="stylesheet" href="https://fonts.googleapis.com/css2?family=Open+Sans:wght@400;600;800&family=Montserrat:wght@400&display=swap">
<style>
  :root {
    --backdrop: #b3b3b3;
    --paper: #ffffff;
    --lavender: #e0e5f8;
    --green: #155233;
    --red: #c21f27;
    --ink: #111111;
    --text: #222222;
  }
  * { margin: 0; padding: 0; box-sizing: border-box; }
  html, body { width: 1200px; height: 1200px; overflow: hidden; }
  body {
    background: var(--backdrop);
    font-family: "Open Sans", Arial, sans-serif;
    position: relative;
  }
  .card {
    position: absolute;
    left: 145px;
    width: 910px;
    height: 528px;
    background: var(--paper);
    overflow: hidden;
  }
  .card-front { top: 0; }
  .card-back { top: 628px; }

  .front-shapes { position: absolute; inset: 0; width: 100%; height: 100%; }

  .holder { position: absolute; left: 106px; top: 98px; }
  .holder-name {
    font-weight: 800;
    font-size: 52px;
    line-height: 1;
    color: var(--ink);
    letter-spacing: -0.5px;
  }
  .holder-title {
    margin-left: 25px;
    margin-top: 2px;
    font-family: "Montserrat", Arial, sans-serif;
    font-size: 14px;
    letter-spacing: 3.2px;
    color: var(--ink);
    text-transform: uppercase;
  }

  .contact { position: absolute; left: 555px; top: 0; list-style: none; }
  .contact-item {
    position: absolute;
    left: 0;
    display: flex;
    align-items: center;
    width: 345px;
    font-size: 19px;
    line-height: 1.35;
    color: var(--text);
  }
  .contact-icon { width: 44px; height: 44px; flex: none; margin-right: 29px; fill: var(--green); }
  .contact-item.email { top: 56px; }
  .contact-item.address { top: 130px; }
  .contact-item.phone { top: 202px; }
  .contact-item.web { top: 276px; }

  .services { position: absolute; left: 80px; top: 384px; list-style: none; }
  .service {
    display: flex;
    align-items: center;
    height: 37.5px;
    font-size: 26px;
    color: #ffffff;
  }
  .service-mark { width: 20px; height: 20px; margin-right: 4px; flex: none; }

  .brand {
    position: absolute;
    left: 0; right: 0;
    top: 262px;
    text-align: center;
    font-size: 66px;
    font-weight: 600;
    color: var(--green);
    letter-spacing: -0.5px;
  }
  .brand-url {
    position: absolute;
    left: 0; right: 0;
    top: 378px;
    text-align: center;
    font-size: 38px;
    color: var(--red);
  }
</style>
</head>
<body>

<section class="card card-front">
  <svg class="front-shapes" viewBox="0 0 758 440" preserveAspectRatio="none" aria-hidden="true">
    <rect x="379" y="0" width="379" height="440" fill="var(--lavender)"/>
    <polygon points="529,367 758,314 758,418" fill="var(--red)"/>
    <polygon points="0,245 758,418 758,440 0,440" fill="var(--green)"/>
  </svg>

  <div class="holder">
    <div class="holder-name">JANE DOE</div>
    <div class="holder-title">Branch Manager</div>
  </div>

  <ul class="contact">
    <li class="contact-item email">
      <svg class="contact-icon" viewBox="0 0 44 44" aria-hidden="true">
        <path d="M5 10h34v3L22 25 5 13z"/>
        <path d="M5 16l17 12 17-12v18H5z"/>
      </svg>
      abcde@crestlinelending.com
    </li>
    <li class="contact-item address">
      <svg class="contact-icon" viewBox="0 0 44 44" aria-hidden="true">
        <path d="M22 4c-7 0-12 5-12 12 0 9 12 24 12 24s12-15 12-24c0-7-5-12-12-12zm0 16a4.5 4.5 0 1 1 0-9 4.5 4.5 0 0 1 0 9z"/>
      </svg>
      <span>48 ridge lane, suite 2<br>Millbrook, Texas 70000</span>
    </li>
    <li class="contact-item phone">
      <svg class="contact-icon" viewBox="0 0 44 44" aria-hidden="true">
        <path d="M11 6l6 0 3 9-4 3c2 5 5 8 10 10l3-4 9 3v6c0 2-2 4-4 4C19 37 7 25 7 10c0-2 2-4 4-4z"/>
      </svg>
      (505) 555-0148
    </li>
    <li class="contact-item web">
      <svg class="contact-icon" viewBox="0 0 44 44" aria-hidden="true">
        <path d="M3 17a27 27 0 0 1 38 0l-3 3a23 23 0 0 0-32 0z"/>
        <path d="M9 23a19 19 0 0 1 26 0l-3 3a14 14 0 0 0-20 0z"/>
        <path d="M15 29a10 10 0 0 1 14 0l-3 3a6 6 0 0 0-8 0z"/>
        <circle cx="22" cy="37" r="3"/>
      </svg>
      www.crestlinelending.com
    </li>
  </ul>

  <ul class="services">
    <li class="service">
      <svg class="service-mark" viewBox="0 0 20 20" aria-hidden="true"><rect x="0" y="0" width="11" height="11" fill="#fff"/><rect x="6" y="7" width="12" height="12" fill="#fff" stroke="var(--green)" stroke-width="1.5"/></svg>
      Title Loans
    </li>
    <li class="service">
      <svg class="service-mark" viewBox="0 0 20 20" aria-hidden="true"><rect x="0" y="0" width="11" height="11" fill="#fff"/><rect x="6" y="7" width="12" height="12" fill="#fff" stroke="var(--green)" stroke-width="1.5"/></svg>
      Personal Loans
    </li>
    <li class="service">
      <svg class="service-mark" viewBox="0 0 20 20" aria-hidden="true"><rect x="0" y="0" width="11" height="11" fill="#fff"/><rect x="6" y="7" width="12" height="12" fill="#fff" stroke="var(--green)" stroke-width="1.5"/></svg>
      Tax Service
    </li>
  </ul>
</section>

<section class="card card-back">
  <div class="brand">Crestline Lending Group</div>
  <div class="brand-url">www.CrestlineLending.com</div>
</section>

</body>
</html>
```